Email Preference Page Design

We are looking for a 2 page design for our users to edit their email preferences and submit friend referrals. You can find the fuctionality, content and text here:

https://brightreel.mailvector.example/app/linkClick/7281/5b9c1d04e6a7f318/20583147/8d4f2a61c0b9e357

* the shipping and billing address might be different so you need to show the billing if the "same as shipping" box is not checked. It can auto-hide like the page above shows if that fits your design.

* when the "unsubscribe from all email lists" box is selected, all the other checkbox options will hide as in the example page. We need you to show us what the site will look like with and without that checkbox selected.

We want to match these two pages to the general feel of these website pages:

www.brightreel.example
and
free.brightreel.example

The page should be very clean and tight. Project is for design only but must be able to be implemented in html showing button and checkbox states. Technically this must be two pages for our system - one for all the user info and one for individual email referrals (see example above).

Target Market(s)

video professionals

Industry/Entity Type

Shipping

Requirements
Must have
• our logo (see numerous versions attached)
well designed header
well designed sections
clean editable text
tight layout
html friendly
easy to understand
2 pages
Nice to have
• custom checkboxes and radio buttons

```html
<!DOCTYPE html>
<html lang="en">
<head>
<meta charset="utf-8">
<title>Subscriber Communication Preferences</title>
<link href="https://fonts.googleapis.com/css2?family=Lato:wght@400;700&display=swap" rel="stylesheet">
<style>
:root{
  --page-bg:#eceef0;
  --panel:#ffffff;
  --panel-edge:#d9dcdf;
  --ink:#2f3c48;
  --ink-soft:#3f4a54;
  --gold:#e7ad2c;
  --gold-light:#fcd66a;
  --gold-dark:#d49a18;
  --cream-top:#fdf7e9;
  --cream-bottom:#f9e8c2;
  --field-edge:#cfd3d7;
  --footer:#e9e6e2;
}
*{box-sizing:border-box;margin:0;padding:0}
html,body{width:909px;height:1200px;overflow:hidden}
body{background:var(--page-bg);font-family:'Lato',sans-serif;color:var(--ink-soft);position:relative}
h1,h2,h3{font-weight:400}
.panel{position:absolute;left:73px;width:761px;background:var(--panel);border:1px solid var(--panel-edge);box-shadow:0 1px 2px rgba(0,0,0,.08);overflow:hidden}
.panel--contact{top:67px;height:520px}
.panel--lists{top:598px;height:520px}
.brand{position:absolute;left:10px;top:7px;width:172px;height:98px;background:#fbfbfb;display:flex;align-items:center;justify-content:center;gap:8px}
.brand__dot{width:14px;height:14px;border-radius:50%;background:var(--gold)}
.brand__name{font-size:26px;font-weight:700;color:var(--ink)}
.page-title{position:absolute;left:336px;top:44px;width:417px;height:40px;border:1px dashed var(--gold);display:flex;align-items:center;justify-content:center;font-size:21px;color:var(--gold)}
.rule{position:absolute;left:10px;right:10px;top:108px;border-top:1px dashed #c9ccd0}
.section-title{position:absolute;left:0;right:0;top:130px;text-align:center;font-size:17px;color:var(--ink)}
.section-title svg{vertical-align:-2px;margin-right:6px}
.field{position:absolute;display:flex;align-items:flex-end;font-size:13px;color:var(--ink)}
.field label{text-align:right;margin-right:10px;line-height:1;padding-bottom:1px}
.field input{width:204px;height:27px;border:1px solid var(--field-edge);border-radius:2px;background:#fff}
.field--left label{width:156px}
.field--right label{width:100px;margin-left:-10px}
.shipping-band{position:absolute;left:0;top:415px;width:761px;height:105px;background:linear-gradient(var(--cream-top),var(--cream-bottom))}
.shipping-title{position:absolute;left:91px;top:437px;font-size:17px;color:var(--ink)}
.check{position:absolute;display:flex;align-items:center;font-size:13px;color:var(--ink)}
.box{width:12px;height:12px;border:1px solid #9aa0a6;background:linear-gradient(#fff,#e6e8ea);margin-right:7px;position:relative;flex:none}
.box--on::after{content:"";position:absolute;left:3px;top:0;width:4px;height:8px;border:solid #3a4f8a;border-width:0 2px 2px 0;transform:rotate(40deg)}
.note{color:var(--gold);margin-left:6px}
.lists-heading{position:absolute;left:92px;top:55px;font-size:17px;font-weight:700;color:var(--ink);letter-spacing:-.3px}
.lists-sub{position:absolute;left:92px;top:91px;font-size:17px;color:var(--ink)}
.options{position:absolute;top:132px;list-style:none}
.options li{height:27.8px;display:flex;align-items:center;font-size:13px;color:var(--ink)}
.options--left{left:92px}
.options--right{left:417px}
.footer-band{position:absolute;left:0;right:0;bottom:0;height:80px;background:var(--footer)}
.save-btn{position:absolute;left:285px;top:16px;width:206px;height:46px;border:1px solid var(--gold-dark);border-radius:2px;background:linear-gradient(var(--gold-light),#f5b92e);font-family:'Lato',sans-serif;font-size:17px;font-weight:700;color:#8a5a08;letter-spacing:-.3px}
</style>
</head>
<body>
<section class="panel panel--contact">
  <div class="brand"><span class="brand__dot"></span><span class="brand__name">BrightReel</span></div>
  <h1 class="page-title">Subscriber Communication Preferences</h1>
  <div class="rule"></div>
  <h2 class="section-title"><svg width="13" height="16" viewBox="0 0 13 16"><path d="M6.5 0C2.9 0 0 2.8 0 6.3 0 10.5 6.5 16 6.5 16S13 10.5 13 6.3C13 2.8 10.1 0 6.5 0z" fill="#e7ad2c"/><circle cx="6.5" cy="6.3" r="2.4" fill="#fff"/></svg>Contact information</h2>

  <div class="field field--left" style="left:0;top:183px"><label>First name</label><input></div>
  <div class="field field--left" style="left:0;top:219px"><label>Email</label><input></div>
  <div class="field field--left" style="left:0;top:254px"><label>Address line 1</label><input></div>
  <div class="field field--left" style="left:0;top:291px"><label>Address line 3</label><input></div>
  <div class="field field--left" style="left:0;top:328px"><label>Country</label><input></div>
  <div class="field field--left" style="left:0;top:365px"><label>Postal code</label><input></div>

  <div class="field field--right" style="left:383px;top:183px"><label>Last name</label><input></div>
  <div class="field field--right" style="left:383px;top:219px"><label>Phone</label><input></div>
  <div class="field field--right" style="left:383px;top:257px"><label>Address line 2</label><input></div>
  <div class="field field--right" style="left:383px;top:294px"><label>City</label><input></div>
  <div class="field field--right" style="left:383px;top:330px"><label>State</label><input></div>

  <div class="shipping-band" role="img" aria-label="Soft cream wave decoration behind the shipping address section"></div>
  <h3 class="shipping-title">Shipping Address</h3>
  <div class="check" style="left:92px;top:468px"><span class="box box--on"></span>My Billing address is same as shipping address.</div>
</section>

<section class="panel panel--lists">
  <div class="check" style="left:92px;top:14px"><span class="box box--on"></span>Subscribe me to your general email list<span class="note">This monthly email includes free video loops and VIP sale notices</span></div>
  <h2 class="lists-heading">Help us filter our emails so we are only sending relevant informationto you</h2>
  <p class="lists-sub">Send me emails about these product types:</p>
  <ul class="options options--left">
    <li><span class="box"></span>Low energy motion loops</li>
    <li><span class="box"></span>High energy motion loops</li>
    <li><span class="box"></span>Timelapse footage</li>
    <li><span class="box"></span>Worship or wedding motion loops</li>
    <li><span class="box"></span>Pre-mixed DVDs and BluRay</li>
    <li><span class="box"></span>Entertainment lasers for concerts and clubs</li>
    <li><span class="box"></span>Entertainment lasers for text &amp; logo display</li>
    <li><span class="box"></span>Custom logo animation services</li>
    <li><span class="box"></span>Video software for creating video animations</li>
    <li><span class="box"></span>Video software for live performance (Vjing)</li>
  </ul>
  <ul class="options options--right">
    <li><span class="box"></span>VJing (live performance video)</li>
    <li><span class="box"></span>DJing (live performance audio+video)</li>
    <li><span class="box"></span>Performing in a band</li>
    <li><span class="box"></span>Video editing</li>
    <li><span class="box"></span>Corporate presentations</li>
    <li><span class="box"></span>Worship video services</li>
    <li><span class="box"></span>Lasers for entertainment &amp; branding</li>
    <li><span class="box"></span>Special offers from BrightReel partners</li>
    <li><span class="box"></span>Unsubscribe from all email lists</li>
  </ul>
  <div class="footer-band"><button class="save-btn">Save My Preferences</button></div>
</section>
</body>
</html>
```